Website for Vayu Kiran Holdings

Need a project marketing website for our company which primarily deals in selling real estate(land sales) from Big Estates to Builders /Clients, help them in Building & Construction and do all Project Management.

Coding

Coded - Design and coding required

Number of Pages Required

4 page

Colors
0054AA
0677BA
7BADD7
CADEEF
E8F1F8
FFC000
F8CF3A
FAE287
FDF2CF
FEFAEE

```html
<!DOCTYPE html>
<html lang="en">
<head>
<meta charset="utf-8">
<title>Vayu Kiran Holdings</title>
<link href="https://fonts.googleapis.com/css2?family=Montserrat:wght@400;500;600;700&family=Poppins:wght@400;500;700;800&family=Playfair+Display:wght@400;500&display=swap" rel="stylesheet">
<style>
:root{
  --blue-dark:#0054AA;--blue:#0677BA;--blue-mid:#7BADD7;--blue-pale:#CADEEF;--blue-wash:#E8F1F8;
  --gold:#FFC000;--gold-soft:#F8CF3A;--gold-pale:#FAE287;--gold-wash:#FDF2CF;
  --ink:#1c1c1c;--text:#333;--footer:#2d343f;--white:#fff;
}
*{box-sizing:border-box;margin:0;padding:0}
html,body{width:1200px;height:2603px;overflow:hidden}
body{position:relative;font-family:"Montserrat",sans-serif;color:var(--text);background:var(--white)}
.abs{position:absolute}
/* hero */
.hero{left:0;top:0;width:1200px;height:716px;background:linear-gradient(180deg,#a9b3d2 0%,#8e9fc8 30%,#6c7fa8 55%,#c59a7a 78%,#3a3a44 100%)}
.nav{left:142px;top:0;width:918px;height:95px;border-bottom:1px solid rgba(255,255,255,.45)}
.brand{left:0;top:30px;font-family:"Montserrat",sans-serif;font-weight:700;font-size:25px;line-height:25px;color:var(--blue-dark);display:flex;align-items:center;gap:10px}
.brand i{display:block;width:70px;height:50px;background:var(--blue-dark)}
.brand.light{color:var(--white)}.brand.light i{background:var(--white)}
.menu{right:0;top:33px;display:flex;align-items:center;gap:0;font-family:"Poppins",sans-serif;font-size:11px;color:var(--white)}
.menu a{color:var(--white);text-decoration:none;margin-right:45px}
.menu .cta{margin:0;background:var(--blue-dark);padding:7px 11px;border-radius:2px}
.hero-box{left:141px;top:257px;width:590px;height:206px;background:rgba(0,84,170,.62);clip-path:polygon(0 0,100% 0,85% 100%,0 100%)}
.hero-title{left:173px;top:297px;font-family:"Poppins",sans-serif;color:var(--white);font-size:35px;line-height:43px}
.hero-title b{font-weight:800}
.hero-band{left:141px;top:392px;width:577px;height:45px;background:var(--white);clip-path:polygon(0 0,100% 0,97% 100%,0 100%);font-family:"Poppins",sans-serif;font-size:17px;color:var(--ink);padding:9px 0 0 16px}
.btn-blue{left:141px;top:489px;width:150px;height:46px;background:var(--blue-dark);border-radius:6px;color:var(--white);font-family:"Poppins",sans-serif;font-size:13px;display:flex;align-items:center;justify-content:center}
/* about */
.about-photo{left:176px;top:785px;width:365px;height:367px;background:linear-gradient(135deg,#4a4d55,#9c8a7e 45%,#d7d1c9 70%,#8a8c92)}
.side-label{left:138px;top:875px;width:16px;height:186px;display:flex;flex-direction:column;align-items:center}
.side-label span{flex:1;width:1px;background:var(--blue-mid)}
.side-label em{font-style:normal;writing-mode:vertical-rl;transform:rotate(180deg);font-size:12px;color:var(--blue-mid);margin:8px 0}
.kicker{font-size:15px;color:var(--ink);display:flex;align-items:center;gap:8px}
.kicker::before{content:"";width:38px;height:1px;background:#999}
.kicker.center::after{content:"";width:38px;height:1px;background:#999}
.serif{font-family:"Playfair Display",serif;font-size:34px;color:var(--ink)}
.serif span{color:var(--blue-dark)}
.about-text{left:656px;top:795px;width:400px}
.about-text h3{font-size:15.5px;font-weight:600;color:var(--blue);margin:10px 0 6px}
.about-text p{font-size:12.5px;line-height:23px;color:var(--text);margin-bottom:4px}
.pill{display:inline-flex;align-items:center;gap:12px;background:var(--gold);border-radius:20px;padding:3px 3px 3px 14px;font-size:13px;font-weight:600;color:var(--ink)}
.pill i{width:29px;height:29px;border-radius:50%;background:var(--blue-dark);display:flex;align-items:center;justify-content:center}
.sketch{left:776px;top:1165px;width:424px;height:95px;background:linear-gradient(180deg,rgba(200,200,200,0),rgba(220,220,220,.5))}
/* services */
.services-bg{left:0;top:1240px;width:1200px;height:612px;background:var(--blue-wash);clip-path:polygon(0 0,60% 33px,100% 48px,100% 100%,0 100%)}
.wedge{left:600px;top:1262px;width:600px;height:90px;background:linear-gradient(90deg,var(--gold-wash),var(--gold-pale));clip-path:polygon(0 10px,100% 0,100% 100%)}
.sec-head{left:0;top:1380px;width:1200px;text-align:center}
.sec-head .kicker{justify-content:center}
.cards{left:141px;top:1471px;width:918px;height:229px;display:flex;border:1px solid var(--blue-pale)}
.card{flex:1;text-align:center;padding:32px 16px 0;border-right:1px solid var(--blue-pale);background:var(--blue-wash)}
.card:last-child{border-right:0}
.card.active{border:2px solid var(--blue-dark);box-shadow:0 4px 10px rgba(0,84,170,.2);margin:-1px 0}
.icon{width:58px;height:58px;margin:0 auto;border-radius:6px;background:linear-gradient(135deg,var(--gold-soft),var(--blue-mid))}
.card h4{font-size:15.5px;font-weight:600;color:var(--ink);margin:22px 0 10px}
.card.active h4{color:var(--blue)}
.card p{font-size:12.5px;line-height:23px}
.view-all{left:544px;top:1730px}
/* features */
.features{left:0;top:1935px;width:1200px}
.feat{position:absolute;width:220px;text-align:center}
.feat .icon{width:54px;height:54px;border-radius:50%}
.feat h5{font-size:15.5px;font-weight:600;color:var(--ink);margin:20px 0 6px}
.feat p{font-size:12.5px;line-height:19px}
/* footer */
.yellow-tri{left:0;top:2160px;width:400px;height:135px;background:var(--gold);clip-path:polygon(0 0,100% 60%,0 100%)}
.footer{left:0;top:2108px;width:1200px;height:495px;background:var(--footer);clip-path:polygon(0 140px,100% 0,100% 100%,0 100%)}
.f-brand{left:142px;top:2350px;width:194px;padding-bottom:18px;border-bottom:1px solid #4d5562}
.socials{left:170px;top:2445px;display:flex;gap:8px}
.socials span{width:28px;height:28px;border-radius:50%;background:var(--gold)}
.fcol h6{font-family:"Playfair Display",serif;font-size:18px;font-weight:500;color:var(--white);margin-bottom:14px}
.fcol li{list-style:none;font-size:12px;color:#e6e6e6;line-height:18.5px;display:flex;align-items:center;gap:6px}
.fcol li::before{content:"";width:8px;height:8px;border-radius:50%;background:var(--blue-mid)}
.contact li::before{display:none}
.contact li{align-items:flex-start;margin-bottom:9px;gap:10px}
.contact svg{flex:none}
.fcol p{font-size:12px;color:#e6e6e6;line-height:18px}
.email{margin-top:18px;width:247px;height:36px;background:var(--white);font-size:11px;color:#555;padding:10px 12px}
.copy{left:0;top:2530px;width:1200px;border-top:1px solid #414955;text-align:center;padding-top:35px;font-size:12.5px;color:#e6e6e6}
</style>
</head>
<body>
<div class="abs hero" role="img" aria-label="Photo of a modern glass office building at sunset"></div>
<header class="abs nav">
  <div class="abs brand"><i></i>VAYU KIRAN<br>HOLDINGS</div>
  <nav class="abs menu"><a>Home</a><a>Projects</a><a>Services</a><a>Contact</a><a class="cta">Get Started</a></nav>
</header>
<div class="abs hero-box"></div>
<h1 class="abs hero-title"><b>Invest in Prime Real Estate</b><br>with Vayu Kiran Holdings</h1>
<div class="abs hero-band">Land Sales, Construction, and Project Management Experts</div>
<div class="abs btn-blue">Contact Us</div>

<div class="abs side-label"><span></span><em>Who we are</em><span></span></div>
<div class="abs about-photo" role="img" aria-label="Photo of an agent with a couple reviewing a house model and tablet"></div>
<section class="abs about-text">
  <div class="kicker">About</div>
  <h2 class="serif"><span>Vayu Kiran</span> Holdings</h2>
  <h3>We Are Investment, Construction, Land Sales Etc..</h3>
  <p>Lorem ipsum dolor sit amet, consectetuer adipiscing elit, sed diam nonummy nibh euismod tincidunt ut laoreet dolore magna aliquam erat volutpat. Ut wisi enim ad minim veniam, quis nostrud exerci tation ullamcorper suscipit lobortis nisl ut aliquip ex ea commodo consequat.</p>
  <p>Duis autem vel eum iriure dolor in hendrerit in vulputate velit esse molestie consequat, vel illum dolore eu feugiat nulla faci ilisis at vero eros et accumsan et iusto odio dignissim qui.</p>
  <div style="margin-top:22px" class="pill">Read More <i><svg width="16" height="12" viewBox="0 0 16 12"><path d="M1 6h13M9 1l5 5-5 5" stroke="#fff" stroke-width="2" fill="none"/></svg></i></div>
</section>
<div class="abs sketch" role="img" aria-label="Line drawing of a stadium building"></div>

<div class="abs services-bg"></div>
<div class="abs wedge"></div>
<div class="abs sec-head"><div class="kicker center">what we do</div><h2 class="serif"><span>Our</span> Services</h2></div>
<div class="abs cards">
  <div class="card"><div class="icon" role="img" aria-label="Investment icon"></div><h4>Investment</h4><p>Duis autem vel eum iriure dolor in hendrerit in vulputate velit esse molestie consequat.</p></div>
  <div class="card active"><div class="icon" role="img" aria-label="Construction icon"></div><h4>Construction</h4><p>Duis autem vel eum iriure dolor in hendrerit in vulputate velit esse molestie consequat.</p></div>
  <div class="card"><div class="icon" role="img" aria-label="Land sales icon"></div><h4>Land Sales</h4><p>Duis autem vel eum iriure dolor in hendrerit in vulputate velit esse molestie consequat.</p></div>
  <div class="card"><div class="icon" role="img" aria-label="Project management icon"></div><h4>Project Management</h4><p>Duis autem vel eum iriure dolor in hendrerit in vulputate velit esse molestie consequat.</p></div>
</div>
<div class="abs view-all pill">View All <i><svg width="16" height="12" viewBox="0 0 16 12"><path d="M1 6h13M9 1l5 5-5 5" stroke="#fff" stroke-width="2" fill="none"/></svg></i></div>

<section class="abs features">
  <div class="feat" style="left:157px"><div class="icon" role="img" aria-label="Partnership icon"></div><h5>Trusted Partner</h5><p>Serving builders and<br>clients with integrity.</p></div>
  <div class="feat" style="left:368px"><div class="icon" role="img" aria-label="Map location icon"></div><h5>Prime Locations</h5><p>Exclusive land in<br>high-demand areas.</p></div>
  <div class="feat" style="left:585px"><div class="icon" role="img" aria-label="Support icon"></div><h5>End-to-End Support</h5><p>From planning to<br>completion.</p></div>
  <div class="feat" style="left:808px"><div class="icon" role="img" aria-label="Process icon"></div><h5>Transparent Process</h5><p>Clear communication<br>at every step.</p></div>
</section>

<div class="abs yellow-tri"></div>
<footer class="abs footer"></footer>
<div class="abs f-brand"><div class="brand light" style="position:static"><i style="width:60px;height:40px"></i>VAYU KIRAN<br>HOLDINGS</div></div>
<div class="abs socials"><span></span><span></span><span></span><span></span></div>
<div class="abs fcol" style="left:380px;top:2352px"><h6>Quick Links</h6><ul><li>Home</li><li>About Us</li><li>Services</li><li>Projects</li><li>Contact Us</li></ul></div>
<div class="abs fcol contact" style="left:543px;top:2352px"><h6>Contact Details</h6><ul>
  <li><svg width="14" height="18" viewBox="0 0 14 18"><path d="M7 1a5 5 0 0 0-5 5c0 4 5 10 5 10s5-6 5-10a5 5 0 0 0-5-5z" fill="none" stroke="#fff" stroke-width="2"/><circle cx="7" cy="6" r="2" fill="#fff"/></svg>123, Building Name, Street<br>City, State XY 123456</li>
  <li><svg width="14" height="14" viewBox="0 0 14 14"><path d="M3 1l2 3-1.5 1.5a8 8 0 0 0 5 5L10 9l3 2-1.5 2.5C6 13 1 8 .5 2.5z" fill="none" stroke="#fff" stroke-width="1.3"/></svg>123 456 7890</li>
  <li><svg width="14" height="11" viewBox="0 0 14 11"><rect x="0" y="0" width="14" height="11" fill="#fff"/><path d="M0 0l7 6 7-6" stroke="#2d343f" stroke-width="1.3" fill="none"/></svg>info@vayukiranholdings.com</li></ul></div>
<div class="abs fcol" style="left:812px;top:2352px"><h6>Newsletter Sign Up</h6><p>Subscribe to our newsletter to get the<br>latest update to your inbox</p><div class="email">Email address</div></div>
<div class="abs copy">© 2025 Vayu Kiran Holdings. All Rights Reserved.</div>
</body>
</html>
```